Two Versions of a Business Card for a Lawyer

Summary: I need a logo and a business card. The business card is two-sided and comes in two versions. One version is conservative, the other is slightly different with one or more pink embellishments in the logo or somewhere else in the business card.
I'm about to start off as a sole practitioner in criminal and immigration law. I'll largely be working with marginalised communities and in areas of social justice. One of my main focuses will be gendered violence, I'm hoping to specialise my practice towards representing victims of domestic and sexual violence and sex workers. I want a business card which would attract this clientele and make them feel safe to speak with me. I'd also like it to communicate a sense of hope.
However, the business card still has to be very conservative as the legal profession is very stuffy. So I was thinking of having two versions of the same card, one would be very straight forward while the other would have a **pink embellishment** or perhaps several. For example, if the scales of justice were used in the design, maybe the second version would have a pink flower about to bloom on the scale somewhere. Or maybe it's my logo that is different and pink.
While both designs have to be pretty conservative, I still want it to give off a sense that I'm alternative and think outside the box. With lawyers, I think a little bit of deviation goes a long way (less is more).
As far as colour goes (other than the pink embellishment), I was thinking something monochromatic, probably black and white but I am open to considering more colours. I personally love colour, and would love to use more colour, but am hesitant because of the nature of the profession. If you can find a way to use more colour while keeping it conservative and letting the pink pop, I'd be pretty pleased.
In general, I would prefer a clean simplistic design and logo. It should be immediately obvious that I'm a lawyer just by glancing at the card. I'm open to symbols of law, like the scales of justice or lady justice or something else. However, I don't want it to be the same as everyone else's.
Eventually, the design/style should be easy to recreate in the form of a website.
As far as the logo goes, it would probably use a circle as my last name starts with the letter "O". It can be very simple, with just my name and "Barrister & Solicitor". I don't currently have a logo, but the winning designer will be invited to provide a separate file for just the logo for an additional fee (I think it was CA$99). (Please ignore the uploaded logo file, it just wouldn't let me continue without uploading something).
As for the information that should go into the card, I'm still finalizing my address and phone number. So please use a placeholder for now.
Target Market(s)
Women, victims of sexual or domestic violence, refugees, people in need of legal services
Industry/Entity Type
Lawyer
Contact Information for Business Card
Mirela Vasquin
Barrister & Solicitor
LL.B., B.C.L., B.F.A.
Criminal & Immigration Law
Street address
Toronto, ON
Postal Code
Phone number
Fax number
Email
Logo Text
Mirela Vasquin, Barrister & Solicitor
Requirements
Must have
- Two versions
- One with pink
- Simplistic
Nice to have
- Maybe more colour
Should not have
- Not too conservative
- Not too predictable

```html
<!DOCTYPE html>
<html lang="en">
<head>
<meta charset="utf-8">
<title>Mirela Vasquin – Business Card</title>
<link href="https://fonts.googleapis.com/css2?family=Open+Sans:wght@400;600;700&display=swap" rel="stylesheet">
<style>
  :root {
    --backdrop: #ecebe8;
    --card: #ffffff;
    --ink: #1a1a1a;
    --pink: #e0489f;
  }
  * { box-sizing: border-box; margin: 0; padding: 0; }
  html, body { width: 1200px; height: 891px; overflow: hidden; }
  body {
    background: var(--backdrop);
    font-family: "Open Sans", Arial, sans-serif;
    color: var(--ink);
    display: flex;
    align-items: center;
    justify-content: center;
    gap: 90px;
  }
  .card {
    position: relative;
    width: 350px;
    height: 612px;
    background: var(--card);
    box-shadow: 0 6px 22px rgba(0,0,0,.12);
    overflow: hidden;
  }
  .card__band {
    position: absolute;
    left: 0; right: 0; bottom: 0;
    height: 16px;
    background: var(--pink);
  }
  .brand-mark {
    width: 78px; height: 78px;
    border: 4px solid var(--ink);
    border-radius: 50%;
  }

  /* Front */
  .card--front .brand {
    position: absolute;
    top: 190px; left: 0; right: 0;
    display: flex; flex-direction: column; align-items: center;
  }
  .card--front .brand-mark { margin-bottom: 26px; }
  .card--front .brand-name {
    font-size: 31px;
    font-weight: 400;
    letter-spacing: .2px;
    padding: 8px 14px;
    border-top: 2px solid var(--pink);
    border-bottom: 2px solid var(--pink);
    line-height: 1.15;
  }

  /* Back */
  .card--back .header {
    position: absolute;
    top: 62px; left: 34px; right: 24px;
    display: flex; align-items: flex-start; gap: 18px;
  }
  .card--back .brand-mark { width: 64px; height: 64px; flex: none; margin-top: 6px; }
  .identity__name {
    font-size: 27px; font-weight: 400; line-height: 1.15;
    padding-bottom: 4px;
    border-bottom: 2px solid var(--pink);
  }
  .identity__title { font-size: 15px; margin-top: 5px; }
  .identity__degrees {
    font-size: 14px; word-spacing: 8px;
    padding-bottom: 6px;
    border-bottom: 2px solid var(--pink);
  }
  .practice {
    position: absolute; top: 218px; left: 34px;
    font-size: 15px;
  }
  .contact {
    position: absolute; top: 262px; left: 34px; right: 24px;
    font-size: 14.5px; line-height: 1.55;
  }
  .contact dt { font-weight: 700; display: inline; }
  .contact dd { display: inline; }
  .contact .row { margin-bottom: 2px; }
</style>
</head>
<body>
  <section class="card card--front" aria-label="Card front">
    <div class="brand">
      <div class="brand-mark" aria-hidden="true"></div>
      <div class="brand-name">Mirela Vasquin</div>
    </div>
    <div class="card__band"></div>
  </section>

  <section class="card card--back" aria-label="Card back">
    <div class="header">
      <div class="brand-mark" aria-hidden="true"></div>
      <div class="identity">
        <div class="identity__name">Mirela Vasquin</div>
        <div class="identity__title">Barrister &amp; Solicitor</div>
        <div class="identity__degrees">LL.B. B.C.L. B.F.A.</div>
      </div>
    </div>
    <p class="practice">Criminal &amp; Immigration Law</p>
    <dl class="contact">
      <div class="row"><dt>Adresse:</dt> <dd>Lorem ipsum dolor<br>ifuim deom dulir Toronto, ON<br>Postal Code:</dd></div>
      <div class="row"><dt>Email:</dt> <dd>mirela.vasquin@mailpost.com</dd></div>
      <div class="row"><dt>Fax:</dt> <dd>&nbsp;&nbsp;&nbsp;00 00 00 00 00</dd></div>
      <div class="row"><dt>Phone:</dt> <dd>&nbsp;00 00 00 00 00</dd></div>
    </dl>
    <div class="card__band"></div>
  </section>
</body>
</html>
```